Improvements to a dating website design

Current site: http://vorlimo.example:8079/pages/index.html

I am looking for an update to our current design that will be more engaging to our users. The current version feels a little too brash and business-like. I would like to make it feel more inviting, to women especially, but men as well. The site is aimed at Indians and other South Asians in their mid 20s to late 30s, living primarily in the U.S. and Canada. It is still under development and not yet live.

This redesign is for the public part of the site, and not the inside pages for member users. To be clear, the sections to be redesigned are:
- the home landing page
- How It Works
- FAQ
- About Us
- Sign Up

Please take the text from the site for the copy.

Thanks, and looking forward to seeing your designs!
Updates

Project Deadline Extended Reason: I would like to give people a little time to develop good ideas. Added Friday, August 21, 2015

Target Market(s)

Our users will be:
- South Asian (indian, Pakistani, Sri Lankan, etc.) single men and women
- in their mid 20s to late 30s
- living primarily in the U.S. and Canada

Industry/Entity Type

Dating

Coding

Coded - Design and coding required

Number of Pages Required

1 page

Requirements
Must have
• I am updating the requirements for this to be a coded HTML/CSS page. (I've also increased the budget, added a 2nd place prize, extended the deadline, and guaranteed payment.) The design should be suitable for "responsiveness" to different browser window sizes, down to mobile phones.
• The main image, which is attached in the files, should continue to be the main image. However, the image can be re-cropped and re-filtered to better match the design. I am happy with the image being used as a full-page backdrop on the home page area, but I'm open to changes.
• All of the text on the current site should be part of the updated design. However, it can be reformatted and laid out differently. (Headings and navigation can be different.)
• The 'What's a Tandem Evening?' section should have the sentences broken out from the single paragraph so that it is easier to read. Each sentence can be a distinct item.
Nice to have
• This site is about online events (called 'Tandem Evenings') where users can meet and get to know each other. So please keep in mind that the point of the website is to
• - educate users how Tandem Evenings work
• - get them to purchase a reservation for the next Tandem Evening (which will be the first).
• Also, the design does not have to be completely different from the existing design, as the site is not yet live and has not been seen by users. Incremental, even small, changes to the current site that result in a captivating design would be just fine.
• Please consider using colors other than the logo colors.
Should not have
• It is not easy to find the right photo, so if you put additional images of people in your design, please make sure they
• - look South Asian (Indian, Pakistani, Sri Lankan, etc.)
• - are wearing western clothing in a western setting
• Also, any images must be available for rights-free licensing. I can't accept submissions that don't follow these guidelines.
• This site is not like other dating sites, in that it has no profiles for users to go through and see. So please don't include any samples of these. Also, no testimonials, as this is a new site.
• There should not be any hearts in the design!
• Any iconified version of the word 'Vorlimo' must be either the actual full-color logo, or a monochrome version of it. Please don't use other word shapes for the site name.

```html
<!DOCTYPE html>
<html lang="en">
<head>
<meta charset="utf-8">
<title>Vorlimo – Tandem Evenings</title>
<link href="https://fonts.googleapis.com/css2?family=Open+Sans:wght@400;600;700&display=swap" rel="stylesheet">
<style>
:root{
  --magenta:#b3197c;
  --magenta-deep:#9c0f69;
  --pink-soft:#e0569f;
  --ink:#2b2b2b;
  --muted:#777;
  --dark:#1c1719;
  --dark-2:#241e21;
  --panel:#ececec;
  --white:#fff;
}
*{box-sizing:border-box;margin:0;padding:0}
html,body{width:1200px;height:2812px;overflow:hidden;background:var(--white)}
body{font-family:"Open Sans",Arial,sans-serif;color:var(--ink)}
.page{position:relative;width:1200px;height:2812px;overflow:hidden}

/* header */
.site-header{position:absolute;left:0;top:0;width:1200px;height:96px;background:var(--white);display:flex;align-items:center;justify-content:space-between;padding:0 72px 0 70px}
.brand{font-size:46px;font-weight:700;color:var(--magenta);letter-spacing:-1px}
.main-nav{display:flex;height:96px}
.main-nav a{display:flex;align-items:center;padding:0 20px;font-size:13px;font-weight:600;color:#555;text-decoration:none;text-transform:uppercase}
.main-nav a.active{background:var(--magenta);color:var(--white)}

/* hero */
.hero{position:absolute;left:0;top:96px;width:1200px;height:616px;background:linear-gradient(100deg,#6b5a4e 0%,#a58a6e 35%,#caa98a 55%,#4a3a33 100%)}
.hero-bubble{position:absolute;left:150px;top:10px}
.hero-copy{position:absolute;left:230px;top:55px;width:470px;text-align:center;color:var(--white);font-size:15px;line-height:1.45}
.hero-copy h1{font-size:26px;font-weight:700;color:var(--pink-soft);margin-bottom:6px}
.hero-copy p{margin-bottom:20px}
.hero-copy .accent{color:var(--pink-soft);font-weight:600}
.hero-dots{position:absolute;left:357px;top:520px;display:flex;gap:10px}
.hero-dots span{width:11px;height:11px;border-radius:50%;background:rgba(255,255,255,.5)}
.hero-dots span.on{background:var(--white)}

/* login bar */
.login-bar{position:absolute;left:0;top:712px;width:1200px;height:88px;background:var(--dark);display:flex;align-items:center;padding:0 70px;color:var(--white);font-size:20px}
.login-bar label{margin-right:12px}
.login-field{width:210px;height:30px;border:1px solid #555;background:#111;color:#888;font-size:11px;padding:7px 10px;margin-right:150px}
.login-field.wide{width:292px;margin-right:32px}
.login-btn{width:176px;height:34px;background:var(--magenta);color:var(--white);font-size:12px;font-weight:700;display:flex;align-items:center;justify-content:center;gap:8px}

/* intro */
.intro{position:absolute;left:0;top:800px;width:1200px;height:300px;text-align:center}
.intro h2{margin-top:52px;font-size:34px;font-weight:700;color:var(--magenta)}
.intro .rule{width:110px;height:3px;background:var(--magenta);margin:10px auto 22px}
.intro p{width:1110px;margin:0 auto;font-size:12.5px;line-height:1.7;color:var(--muted)}
.btn{display:inline-flex;align-items:center;justify-content:center;background:var(--magenta);color:var(--white);font-size:12px;font-weight:700;text-transform:uppercase;height:34px;padding:0 26px}
.intro .btn{margin-top:24px}

/* how it works */
.how{position:absolute;left:0;top:1100px;width:1200px;height:920px;background:var(--panel)}
.how h2{text-align:center;margin-top:30px;font-size:34px;color:var(--magenta);font-weight:700}
.how .rule{width:110px;height:3px;background:var(--magenta);margin:10px auto 0}
.tile{position:absolute}
.tile-main{left:48px;top:92px;width:544px;height:508px;background:linear-gradient(160deg,#b23a83,#8e2f6c 60%,#c25a96)}
.tile-main .tile-text{position:absolute;left:90px;top:300px;width:370px;color:var(--white);font-size:12px;line-height:1.5;text-align:center}
.tile-main .btn{position:absolute;left:206px;top:370px;height:30px;font-size:11px;background:var(--magenta-deep)}
.tile-a{left:600px;top:92px;width:552px;height:248px;background:linear-gradient(180deg,#9fc1de,#d9d3c6)}
.tile-b{left:600px;top:348px;width:552px;height:252px;background:linear-gradient(180deg,#dfe3e6,#c9b7a3)}
.tile-c{left:48px;top:608px;width:544px;height:280px;background:linear-gradient(180deg,#7fa6d4,#5b4a3d)}
.tile-d{left:600px;top:608px;width:552px;height:280px;background:linear-gradient(180deg,#b8c7d6,#8b7465)}

/* sign band */
.sign-band{position:absolute;left:0;top:2020px;width:1200px;height:140px;background:linear-gradient(90deg,#4a1f35,#9a4a5e 50%,#3d1a2c);display:flex;justify-content:center;align-items:center;gap:88px}
.sign-btn{width:292px;height:64px;border:4px solid rgba(255,255,255,.5);display:flex;align-items:center;justify-content:center;gap:12px;font-size:18px;font-weight:600}
.sign-btn.in{background:#f3d2e3;color:var(--magenta)}
.sign-btn.up{background:var(--magenta);color:var(--white)}

/* faq + about */
.info{position:absolute;left:0;top:2160px;width:1200px;height:412px;background:var(--dark-2);color:#ccc}
.faq{position:absolute;left:60px;top:42px;width:620px}
.info h3{font-size:28px;font-weight:700;color:var(--magenta);margin-bottom:18px}
.faq li{list-style:none;font-size:13px;line-height:30px;display:flex;align-items:center;gap:12px}
.faq li::before{content:"";width:8px;height:8px;background:var(--magenta);border-radius:50%;flex:none}
.faq li.current{color:var(--pink-soft)}
.about{position:absolute;left:688px;top:42px;width:460px}
.about p{font-size:12.5px;line-height:1.75}
.about .btn{margin-top:22px}

/* contact */
.contact{position:absolute;left:0;top:2572px;width:1200px;height:160px;background:linear-gradient(90deg,#2a1827,#3a1f33 50%,#2a1827);color:var(--white);font-size:20px}
.contact-item{position:absolute;display:flex;align-items:center;gap:26px}
.contact-item svg{flex:none}

/* footer */
.site-footer{position:absolute;left:0;top:2732px;width:1200px;height:80px;background:var(--magenta);color:var(--white);font-size:11px;display:flex;align-items:center;justify-content:center}
.social{position:absolute;right:60px;top:26px;display:flex;gap:10px}
.social span{width:28px;height:28px;background:var(--white)}
</style>
</head>
<body>
<div class="page">

  <header class="site-header">
    <div class="brand">vorlimo</div>
    <nav class="main-nav">
      <a class="active">Home</a>
      <a>How it works</a>
      <a>About us</a>
      <a>FAQ's</a>
      <a>Sign up</a>
    </nav>
  </header>

  <section class="hero" role="img" aria-label="Photo of a smiling young couple sitting together in a warm café">
    <svg class="hero-bubble" width="610" height="560" viewBox="0 0 610 560" aria-hidden="true">
      <path d="M40 30 Q305 -10 570 30 Q610 280 570 520 Q305 565 40 520 Q0 280 40 30 Z" fill="rgba(34,22,20,.82)"/>
    </svg>
    <div class="hero-copy">
      <h1>CHEMISTRY</h1>
      <p>That little sizzle when you look over.<br>The charming banter with those electric undertones.<br>That mysterious, undeniable, necessary connection.</p>
      <p class="accent">But can you feel it from a profile alone?</p>
      <p>Will you actually get along together? Do you agree on the important things?<br>Would your family like them?</p>
      <p>It seems so hopelessly complicated, and it takes so much time<br>to understand. And we've got the perfect answer.</p>
      <p class="accent">Introducing the Vorlimo Tandem Evening. Meet, talk, and feel it.</p>
    </div>
    <div class="hero-dots"><span class="on"></span><span></span></div>
  </section>

  <form class="login-bar">
    <label>Email :</label>
    <div class="login-field">Enter Email Address</div>
    <label>Password:</label>
    <div class="login-field wide">Enter Your Password</div>
    <div class="login-btn">
      <svg width="12" height="12" viewBox="0 0 12 12" aria-hidden="true"><rect x="2" y="5" width="8" height="7" fill="#fff"/><path d="M3.5 5V3.5a2.5 2.5 0 0 1 5 0V5" stroke="#fff" stroke-width="1.4" fill="none"/></svg>
      LOG IN
    </div>
  </form>

  <section class="intro">
    <h2>What's a Tandem Evening?</h2>
    <div class="rule"></div>
    <p>It's a fully realized speed dating event for the digital age. We ask you some deep questions about who you are and what you are looking for. You show us when you feel<br>attractive. We use those insights to invite you to a private live event with the perfect dates for tonight, and maybe forever. And if something clicks between you, you'll both<br>know right away, with a few minutes of real conversation instead of endless messages. It's easy, it's fun, and it's built around real chemistry, not only a profile.</p>
    <a class="btn">Read more</a>
  </section>

  <section class="how">
    <h2>How It Works</h2>
    <div class="rule"></div>
    <div class="tile tile-main" role="img" aria-label="Photo of a young man on a city street, tinted magenta">
      <p class="tile-text">1. When you sign up, you will answer a profile questionnaire that will tell us about yourself in a deep and meaningful way.</p>
      <a class="btn">Read more</a>
    </div>
    <div class="tile tile-a" role="img" aria-label="Photo of a cheerful woman with raised arms outdoors"></div>
    <div class="tile tile-b" role="img" aria-label="Photo of a smiling woman in a bright room"></div>
    <div class="tile tile-c" role="img" aria-label="Photo of a man looking through binoculars"></div>
    <div class="tile tile-d" role="img" aria-label="Photo of a group of friends celebrating"></div>
  </section>

  <section class="sign-band" role="img" aria-label="Blurred warm city-lights backdrop">
    <div class="sign-btn in">
      <svg width="18" height="18" viewBox="0 0 18 18" aria-hidden="true"><rect x="3" y="8" width="12" height="9" fill="#b3197c"/><path d="M5.5 8V5.5a3.5 3.5 0 0 1 7 0V8" stroke="#b3197c" stroke-width="2" fill="none"/></svg>
      Sign In
    </div>
    <div class="sign-btn up">
      <svg width="18" height="18" viewBox="0 0 18 18" aria-hidden="true"><path d="M2 16 L16 2 M9 2 H16 V9" stroke="#fff" stroke-width="2.2" fill="none"/></svg>
      Sign Up
    </div>
  </section>

  <section class="info">
    <div class="faq">
      <h3>FAQ</h3>
      <ul>
        <li class="current">What does a Tandem Evening involve?</li>
        <li>What are the technology requirements to be able to take part in the event?</li>
        <li>Is it possible to test my system to see if it will work in the event?</li>
        <li>What will other users know about me?</li>
        <li>How long does the profile questionnaire take?</li>
        <li>Does a MATCH who doesn't choose me back know that I picked them?</li>
        <li>Will you match me with people close by?</li>
      </ul>
    </div>
    <div class="about">
      <h3>About Us</h3>
      <p>We started Vorlimo because meeting the right person should feel natural, warm and a little bit exciting. Our team brings people together through small live events built around real conversation, shared values and genuine chemistry, so every evening feels personal and worth your time.</p>
      <a class="btn">Read more</a>
    </div>
  </section>

  <section class="contact">
    <div class="contact-item" style="left:92px;top:36px">
      <svg width="26" height="26" viewBox="0 0 24 24" aria-hidden="true"><path d="M6.6 10.8a15 15 0 0 0 6.6 6.6l2.2-2.2a1 1 0 0 1 1-.25 11.4 11.4 0 0 0 3.6.57 1 1 0 0 1 1 1V20a1 1 0 0 1-1 1A17 17 0 0 1 3 4a1 1 0 0 1 1-1h3.5a1 1 0 0 1 1 1c0 1.25.2 2.45.57 3.57a1 1 0 0 1-.25 1z" fill="#fff"/></svg>
      123.456.7890
    </div>
    <div class="contact-item" style="left:430px;top:36px">
      <svg width="26" height="26" viewBox="0 0 24 24" aria-hidden="true"><rect x="3" y="4" width="18" height="16" rx="2" fill="#fff"/><rect x="6" y="7" width="12" height="4" fill="#3a1f33"/></svg>
      123.456.7890
    </div>
    <div class="contact-item" style="left:770px;top:36px">
      <svg width="26" height="26" viewBox="0 0 24 24" aria-hidden="true"><circle cx="12" cy="12" r="10" fill="#fff"/><path d="M6 9l6 4 6-4" stroke="#3a1f33" stroke-width="2" fill="none"/></svg>
      info@vorlimo.example
    </div>
    <div class="contact-item" style="left:92px;top:96px">
      <svg width="26" height="26" viewBox="0 0 24 24" aria-hidden="true"><path d="M12 2a7 7 0 0 1 7 7c0 5-7 13-7 13S5 14 5 9a7 7 0 0 1 7-7z" fill="#fff"/><circle cx="12" cy="9" r="2.5" fill="#3a1f33"/></svg>
      Address Line1, Address line2, -123456, Country.
    </div>
  </section>

  <footer class="site-footer">
    All Rights Reserved. Copyright 2015 Vorlimo
    <div class="social"><span></span><span></span><span></span></div>
  </footer>

</div>
</body>
</html>
```